Ronan Pike Building Business Card Design

Hi,

I need a business card for my Building company.
I am a Builder and build homes for clients.
I am looking for a sophisticated logo that can be used on business cards, envelopes and letter heads.
I am trying to take my business to the next level and need a professional business card.

Colours: Please use white, black, dark grey and bright blue.

Thank you,

Marnie and Ronan.

Target Market(s)

1. Home and Building Companies 2. Potential customers

Industry/Entity Type

Business

Contact Information for Business Card

Ronan Pike Building PTY LTD

Ronan Pike

Director

A.B.N. 37 902 518 617

BUILDERS LICENCE No. 573019k

Mobile: 0471 283 906

Email: ronanpikebuilding@maildrop-example.com.au

Requirements
Must have
• The following is compulsory to have in the designs:

Ronan Pike Building PTY LTD (business name)

Ronan Pike (contact name)

Director (position)

A.B.N. 37 902 518 617

Builders Licence No. 573019k

Mobile: 0471 283 906

Nice to have
• Logo for business
Should not have
• Should not be cluttered.

I am looking for a clean, sophisticated and professional business card design.

```html
<!DOCTYPE html>
<html lang="en">
<head>
<meta charset="utf-8">
<title>Ronan Pike Building – Business Card</title>
<link rel="stylesheet" href="https://fonts.googleapis.com/css2?family=Source+Sans+3:ital,wght@0,400;0,700;1,400;1,700&display=swap">
<style>
  :root {
    --card-black: #1f1d1e;
    --dark-grey: #3a3a3d;
    --dark-grey-soft: #2c2b2d;
    --brand-blue: #1d8bf2;
    --text-white: #ffffff;
    --text-soft: #eeeeee;
  }
  * { margin: 0; padding: 0; box-sizing: border-box; }
  html, body {
    width: 1200px;
    height: 848px;
    overflow: hidden;
  }
  body {
    font-family: "Source Sans 3", "Myriad Pro", Arial, sans-serif;
    background: var(--card-black);
  }
  .business-card {
    position: relative;
    width: 1200px;
    height: 848px;
    background: var(--card-black);
    color: var(--text-white);
  }
  .logo-symbol-area {
    position: absolute;
    left: 150px;
    top: 60px;
    width: 930px;
    height: 200px;
    background: linear-gradient(180deg, var(--dark-grey-soft), var(--dark-grey));
  }
  .brand-name {
    position: absolute;
    left: 100px;
    top: 272px;
    width: 990px;
    font-weight: 700;
    font-size: 92px;
    line-height: 1;
    letter-spacing: 2px;
    text-transform: uppercase;
    white-space: nowrap;
    color: var(--text-white);
  }
  .brand-suffix {
    display: block;
    text-align: right;
    font-size: 40px;
    letter-spacing: 8px;
    margin-top: 2px;
  }
  .registration-line {
    position: absolute;
    left: 104px;
    top: 430px;
    font-size: 25px;
    color: var(--text-soft);
  }
  .contact-person {
    position: absolute;
    left: 0;
    right: 0;
    top: 510px;
    text-align: center;
    font-weight: 700;
    font-size: 46px;
    color: var(--brand-blue);
  }
  .contact-person .role { font-style: italic; }
  .contact-band {
    position: absolute;
    left: 0;
    right: 0;
    bottom: 0;
    height: 200px;
    background: var(--brand-blue);
    display: flex;
    align-items: center;
    padding-left: 70px;
    font-size: 34px;
    color: var(--text-white);
    white-space: nowrap;
  }
  .contact-band .phone {
    font-weight: 700;
    font-size: 44px;
  }
  .contact-band .separator {
    font-weight: 700;
    margin: 0 12px;
  }
  .contact-band .email { font-style: italic; }
</style>
</head>
<body>
  <main class="business-card">
    <div class="logo-symbol-area" role="img" aria-label="Company logo symbol area: house roof outlines"></div>
    <h1 class="brand-name">Ronan Pike Building<span class="brand-suffix">PTY LTD</span></h1>
    <p class="registration-line">A.B.N. 37 902 518 617 • Builders Licence No. 573019k</p>
    <p class="contact-person">Ronan Pike - <span class="role">Director</span></p>
    <footer class="contact-band">
      <span class="phone">m: 0471 283 906</span>
      <span class="separator">•</span>
      <span class="email-label">e:&nbsp;</span><span class="email">ronanpikebuilding@maildrop-example.com.au</span>
    </footer>
  </main>
</body>
</html>
```